Business Cards

I'd like help creating business cards with the full logo "Veltrona Capital Partners" on the back of the card (navy background with white writing), and abbreviated logo "VCP" on the front. Would like to list name, title, phone number, email, and website listed on front of card. Would like to keep very simple. Front font Arial or similar.

```html
<!DOCTYPE html>
<html lang="en">
<head>
<meta charset="utf-8">
<title>Veltrona Capital Partners — Business Cards</title>
<link rel="stylesheet" href="https://fonts.googleapis.com/css2?family=Lato:wght@400;700&family=Montserrat:wght@500;700&display=swap">
<style>
  :root {
    --navy: #1e366b;
    --white: #ffffff;
    --ink-gray: #7d7f86;
    --rule-gray: #a9abb0;
    --ghost: #ecedf3;
    --backdrop-top: #45474b;
    --backdrop-bottom: #1f2022;
  }
  html, body {
    margin: 0;
    width: 1200px;
    height: 952px;
    overflow: hidden;
  }
  body {
    background: radial-gradient(ellipse at 60% 35%, var(--backdrop-top), var(--backdrop-bottom) 75%);
    font-family: "Lato", Arial, sans-serif;
    position: relative;
  }
  .card {
    position: absolute;
    width: 540px;
    height: 308px;
    border-radius: 18px;
    box-shadow: 0 14px 30px rgba(0,0,0,0.45);
    overflow: hidden;
  }
  /* Back side */
  .card--back {
    left: 70px;
    top: 520px;
    background: var(--navy);
    display: flex;
    align-items: center;
    justify-content: center;
  }
  .brand-name--back {
    color: var(--white);
    font-family: "Montserrat", Arial, sans-serif;
    font-weight: 700;
    font-size: 34px;
    letter-spacing: 1px;
    text-transform: uppercase;
    text-align: center;
    line-height: 1.25;
  }
  /* Front side */
  .card--front {
    left: 590px;
    top: 130px;
    background: var(--white);
  }
  .brand-name--front {
    position: absolute;
    left: 32px;
    top: 28px;
    color: var(--navy);
    font-family: "Montserrat", Arial, sans-serif;
    font-weight: 700;
    font-size: 17px;
    letter-spacing: 0.5px;
    text-transform: uppercase;
    line-height: 1.25;
  }
  .contact-list {
    position: absolute;
    left: 32px;
    top: 118px;
    margin: 0;
    padding: 0;
    list-style: none;
    color: var(--ink-gray);
    font-size: 12px;
    line-height: 1.3;
  }
  .contact-item {
    display: flex;
    align-items: flex-start;
    gap: 9px;
    margin-bottom: 9px;
  }
  .contact-icon {
    flex: 0 0 15px;
    width: 15px;
    height: 15px;
    background: var(--navy);
    border-radius: 2px;
    display: flex;
    align-items: center;
    justify-content: center;
  }
  .contact-icon svg { width: 11px; height: 11px; }
  .person {
    position: absolute;
    right: 34px;
    top: 110px;
    text-align: right;
  }
  .person-name {
    margin: 0;
    color: var(--navy);
    font-family: "Montserrat", Arial, sans-serif;
    font-size: 19px;
    letter-spacing: 0.5px;
    text-transform: uppercase;
    font-weight: 500;
  }
  .person-name .surname { font-weight: 700; }
  .person-title {
    margin: 4px 0 0;
    color: var(--ink-gray);
    font-size: 15px;
  }
  .person-rule {
    width: 62px;
    height: 1px;
    background: var(--rule-gray);
    margin: 8px 0 0 auto;
  }
  .monogram {
    position: absolute;
    right: 40px;
    bottom: 18px;
    color: var(--ghost);
    font-family: "Montserrat", Arial, sans-serif;
    font-weight: 700;
    font-size: 78px;
    letter-spacing: 2px;
    line-height: 1;
  }
</style>
</head>
<body>

  <section class="card card--front" aria-label="Business card front">
    <div class="brand-name--front">Veltrona<br>Capital Partners</div>

    <ul class="contact-list">
      <li class="contact-item">
        <span class="contact-icon">
          <svg viewBox="0 0 12 12"><path d="M6 1a3.2 3.2 0 0 0-3.2 3.2C2.8 6.8 6 11 6 11s3.2-4.2 3.2-6.8A3.2 3.2 0 0 0 6 1zm0 4.5a1.3 1.3 0 1 1 0-2.6 1.3 1.3 0 0 1 0 2.6z" fill="#fff"/></svg>
        </span>
        <span>2150 Harbor Crest Avenue<br>Arlington, VA 22201</span>
      </li>
      <li class="contact-item">
        <span class="contact-icon">
          <svg viewBox="0 0 12 12"><path d="M3 1.2l1.6 2.4-1 1c.6 1.3 1.5 2.2 2.8 2.8l1-1L9.8 8 9 10.2C5 10 2 7 1.8 3z" fill="#fff"/></svg>
        </span>
        <span>+00 987 654 32</span>
      </li>
      <li class="contact-item">
        <span class="contact-icon">
          <svg viewBox="0 0 12 12"><rect x="1.5" y="3" width="9" height="6" fill="none" stroke="#fff" stroke-width="1"/><path d="M1.5 3L6 6.5 10.5 3" fill="none" stroke="#fff" stroke-width="1"/></svg>
        </span>
        <span>hello@veltronacap.com</span>
      </li>
      <li class="contact-item">
        <span class="contact-icon">
          <svg viewBox="0 0 12 12"><circle cx="6" cy="6" r="4.3" fill="none" stroke="#fff" stroke-width="1"/><path d="M1.7 6h8.6M6 1.7c-2 2.4-2 6.2 0 8.6M6 1.7c2 2.4 2 6.2 0 8.6" fill="none" stroke="#fff" stroke-width="0.9"/></svg>
        </span>
        <span>www.veltronacap.com</span>
      </li>
    </ul>

    <div class="person">
      <h1 class="person-name">Daniel R. <span class="surname">Whitford</span></h1>
      <p class="person-title">Managing Director</p>
      <div class="person-rule"></div>
    </div>

    <div class="monogram" aria-hidden="true">VCP</div>
  </section>

  <section class="card card--back" aria-label="Business card back">
    <div class="brand-name--back">Veltrona<br>Capital Partners</div>
  </section>

</body>
</html>
```